VaultMeridan Business Card Re-Design

VaultMeridan is a specialized information security company that applies its proven methodology of security Assessment, Development, Integration and Training (A-D-I-T) to provide cyber security services in the areas of Data Protection, Network Defense and Compliance. We need the current business card re-designed to properly scale the fonts and possibly rearranging some elements (icons, lettering, etc.) to make the card more appealing to the eye. The card should have the logo that is on the web site (www.vaultmeridan-example.com). We would like ideas for both a black card (black background) and a white card (white background). We prefer rounded corners to help the card stand out but are open to all ideas. FYI: VaultMeridan's slogan is "...your security is our business".

Target Market(s)

#1 US Government Contracting Companies, #2 Commercial Companies, #3 Gen. Public.

Industry/Entity Type

Business

Contact Information for Business Card

See Description; open to the use of different fonts.

Font styles to use
Sans Serif

Colors
000000
ec1f27
ffffff

Requirements
Must have
• Company logo on web site, rounded corners, list of company offerings on the back of the card.
Nice to have
• Icons
Should not have
• none

```html
<!DOCTYPE html>
<html lang="en">
<head>
<meta charset="utf-8">
<title>VaultMeridan Business Card</title>
<link rel="stylesheet" href="https://fonts.googleapis.com/css2?family=Lato:wght@400;700&family=Crimson+Text:wght@400;600&display=swap">
<style>
  :root {
    --stage: #2a2a2a;
    --card: #1c1c1d;
    --card-edge: #2c2c2e;
    --red: #ec1f27;
    --red-deep: #b3161c;
    --white: #ffffff;
    --soft-white: #e6e6e6;
    --grey: #8a8a8a;
    --map-tone: #333335;
  }
  * { box-sizing: border-box; margin: 0; padding: 0; }
  html, body {
    width: 1200px; height: 873px; overflow: hidden;
    background: var(--stage);
    font-family: "Lato", sans-serif;
  }
  .canvas { position: relative; width: 1200px; height: 873px; }

  .card {
    position: absolute;
    width: 540px; height: 309px;
    border-radius: 18px;
    background: linear-gradient(160deg, var(--card-edge), var(--card) 55%);
    box-shadow: 0 14px 40px rgba(0,0,0,.55);
    overflow: hidden;
  }

  /* ---------- back ---------- */
  .card-back { left: 60px; top: 100px; text-align: center; }
  .back-brand {
    margin-top: 44px;
    display: flex; align-items: center; justify-content: center; gap: 12px;
  }
  .brand-square { width: 18px; height: 18px; background: var(--red); }
  .back-brand .brand-name {
    font-size: 32px; font-weight: 700; letter-spacing: 6px;
    color: var(--white); text-transform: uppercase;
  }
  .brand-rule {
    width: 250px; height: 1px; margin: 14px auto 16px;
    background: var(--grey);
  }
  .services { list-style: none; color: var(--soft-white); font-size: 10px; line-height: 17px; }
  .services .sep { color: var(--red); margin: 0 4px; }
  .back-web {
    margin-top: 14px;
    display: flex; align-items: center; justify-content: center; gap: 12px;
    color: var(--red); font-size: 11px; font-weight: 700; letter-spacing: 1.5px;
  }
  .back-web::before, .back-web::after {
    content: ""; width: 70px; height: 1px; background: var(--grey);
  }

  /* ---------- front ---------- */
  .card-front { left: 600px; top: 464px; }
  .world-map {
    position: absolute; left: 110px; top: 40px; width: 390px; height: 200px;
    background: radial-gradient(ellipse at 50% 50%, var(--map-tone), transparent 70%);
    opacity: .9;
  }
  .front-brand {
    position: absolute; left: 30px; top: 40px;
    display: flex; align-items: center; gap: 10px;
  }
  .brand-circle { width: 22px; height: 22px; border-radius: 50%; background: var(--red); }
  .front-brand .brand-name { font-size: 26px; font-weight: 700; color: var(--white); }

  .person {
    position: absolute; right: 54px; top: 70px;
    display: flex; align-items: flex-start; gap: 8px;
    font-family: "Crimson Text", serif; color: var(--soft-white);
  }
  .person-name { font-size: 22px; font-weight: 600; padding-top: 10px; }
  .person-meta { font-size: 13px; line-height: 16px; font-weight: 600; }

  .accent-line {
    position: absolute; left: 26px; right: 120px; top: 142px;
    height: 2px; background: linear-gradient(90deg, var(--red-deep), var(--red));
  }

  .contacts {
    position: absolute; left: 32px; top: 162px; list-style: none;
    font-family: "Crimson Text", serif; color: var(--soft-white); font-size: 16px;
  }
  .contacts li { display: flex; align-items: center; gap: 14px; height: 27px; }
  .contacts svg { width: 14px; height: 14px; fill: var(--red); flex: none; }

  .address {
    position: absolute; right: 30px; top: 200px; text-align: right;
    font-family: "Crimson Text", serif; color: var(--red); font-size: 16px; line-height: 22px;
  }
</style>
</head>
<body>
<main class="canvas">

  <section class="card card-back" aria-label="Business card back">
    <div class="back-brand">
      <span class="brand-square"></span>
      <span class="brand-name">VaultMeridan</span>
    </div>
    <div class="brand-rule"></div>
    <ul class="services">
      <li>Red/Blue Team<span class="sep">|</span>Secure Virtual Computing<span class="sep">|</span>Data Center Consolidation</li>
      <li>Classified Cross Domain Solutions<span class="sep">|</span>Secure Cloud &amp; Open Stack Solutions</li>
      <li>Network Attack Penetration &amp; Defense<span class="sep">|</span>Data Encrypting/Privacy<span class="sep">|</span>Secure Wireless Solutions</li>
      <li>Certification &amp; Accreditation<span class="sep">|</span>Security Subject Matter Experts</li>
      <li>Executive Security Strategy Coaching<span class="sep">|</span>Foreign/Counter Intelligence Data Security</li>
      <li>Security Training, Assessment &amp; Integration</li>
    </ul>
    <p class="back-web">www.vaultmeridan-example.com</p>
  </section>

  <section class="card card-front" aria-label="Business card front">
    <div class="world-map" role="img" aria-label="Faint dotted world map in dark grey and red"></div>

    <div class="front-brand">
      <span class="brand-circle"></span>
      <span class="brand-name">VaultMeridan</span>
    </div>

    <div class="person">
      <span class="person-name">Darren Holt</span>
      <span class="person-meta">CISSP, C|EH<br>President CEO</span>
    </div>

    <div class="accent-line"></div>

    <ul class="contacts">
      <li>
        <svg viewBox="0 0 16 16" aria-hidden="true"><path d="M2 5c0-2 2-3 6-3s6 1 6 3v1h-3V5H5v1H2z M4 7h8l2 6H2z M8 8.5a2 2 0 1 0 0 4 2 2 0 0 0 0-4z"/></svg>
        <span>555 010 1201</span>
      </li>
      <li>
        <svg viewBox="0 0 16 16" aria-hidden="true"><path d="M4 1h8v14H4z M5.5 2.5v9h5v-9z M7 12.5h2v1H7z"/></svg>
        <span>555 010 1627</span>
      </li>
      <li>
        <svg viewBox="0 0 16 16" aria-hidden="true"><path d="M1 3h14v10H1z M2 4l6 5 6-5"/></svg>
        <span>info@vaultmeridan-example.com</span>
      </li>
      <li>
        <svg viewBox="0 0 16 16" aria-hidden="true"><path d="M1 3h14v10H1z M2 4l6 5 6-5"/></svg>
        <span>dholt@vaultmeridan-example.com</span>
      </li>
    </ul>

    <p class="address">1420 Harbor Crest Rd<br>Suite 210 Easton, Maryland 21601</p>
  </section>

</main>
</body>
</html>
```